Business card for STEADYLINE

Please design professional business card for IT consulting firm STEADYLINE INC.
Use logo attached.
Use information from sample tRove business card attached.
replace trove inc with STEADYLINE INC.
as well as troveinc.com with steadyline.example

```html
<!DOCTYPE html>
<html lang="en">
<head>
<meta charset="utf-8">
<title>STEADYLINE Business Card</title>
<link href="https://fonts.googleapis.com/css2?family=Montserrat:ital,wght@0,400;0,500;0,600;0,700;1,400&display=swap" rel="stylesheet">
<style>
  :root {
    --page: #fdfdfd;
    --card-front: #f6f6f6;
    --card-back: #030e13;
    --frame: #6f6f6f;
    --ink: #111417;
    --ink-soft: #2c2a2a;
    --muted: #a9a9a9;
    --white: #ffffff;
    --accent: #3fc8dc;
  }
  * { margin: 0; padding: 0; box-sizing: border-box; }
  html, body {
    width: 1200px; height: 1057px; overflow: hidden;
    background: var(--page);
    font-family: "Montserrat", Arial, sans-serif;
  }
  .canvas { position: relative; width: 1200px; height: 1057px; }
  .card { position: absolute; left: 333px; width: 535px; height: 306px; }
  .card-front { top: 203px; background: var(--card-front); border: 1px solid var(--frame); }
  .card-back { top: 550px; background: var(--card-back); }

  .wordmark { display: flex; align-items: center; gap: 9px; }
  .wordmark-name {
    font-weight: 700; font-size: 30px; letter-spacing: 1.5px; line-height: 1;
  }
  .wordmark-square { width: 18px; height: 18px; background: var(--accent); }
  .card-front .wordmark { position: absolute; left: 105px; top: 42px; }
  .card-front .wordmark-name { color: var(--ink); }
  .card-back .wordmark {
    position: absolute; left: 50%; top: 50%; transform: translate(-50%, -50%);
  }
  .card-back .wordmark-name { color: var(--white); }

  .details { position: absolute; left: 105px; top: 97px; color: var(--ink); }
  .job-title {
    font-style: italic; font-weight: 400; font-size: 14.5px; color: var(--muted);
    letter-spacing: 0.3px; line-height: 18px;
  }
  .person-name {
    margin-top: 7px; font-weight: 600; font-size: 16px; color: var(--ink-soft);
    letter-spacing: 0.4px; line-height: 20px;
  }
  .contact { margin-top: 15px; font-size: 12.8px; line-height: 17.5px; }
  .contact b { font-weight: 700; }
  .contact em { font-style: italic; }
  .company {
    margin-top: 16px; font-weight: 600; font-size: 14.5px; line-height: 18px;
    letter-spacing: 0.2px;
  }
  .address { margin-top: 1px; font-size: 13px; line-height: 17.5px; }
</style>
</head>
<body>
<div class="canvas">
  <section class="card card-front">
    <div class="wordmark">
      <span class="wordmark-name">STEADYLINE</span>
      <span class="wordmark-square"></span>
    </div>
    <div class="details">
      <p class="job-title">GENERAL MANAGER</p>
      <p class="person-name">MAREK HALVORSEN, P.ENG</p>
      <div class="contact">
        <p><b>o.</b> (555) 286-0170 ext.201 c. (555) 897-0169</p>
        <p><b>e.</b> mhalvorsen@steadyline.example - <em>steadyline.example</em></p>
      </div>
      <p class="company">STEADYLINE INC</p>
      <div class="address">
        <p>2718 Ardent Rd., Suite 101</p>
        <p>Brookfield, Ontario, A1B 2C3, Canada</p>
      </div>
    </div>
  </section>

  <section class="card card-back">
    <div class="wordmark">
      <span class="wordmark-name">STEADYLINE</span>
      <span class="wordmark-square"></span>
    </div>
  </section>
</div>
</body>
</html>
```